Herbal tea shop web designing - Brewvine

We need a business-charity purpose online shop selling premium herbal teas with a tagline "Healthy with a heart" where all the raw materials are being purchased from Indonesian local farmers in order to give them sustainable employment. Every 20% from the total amount of the customer's purchase from our website always goes back to their communities to help build better sanitation, education or whatever they need. We need page to blog too and another page for customers to interact and share their thought. we expect an eye catching simple earthy (maybe a bit rustic) design with some brush lettering font in some parts. Thank you.

Target Market(s)

-Tea Lovers
-Anyone with body weight issues or any health issues in general

Industry/Entity Type

Home Health Care

Number of Pages Required

5+ page

Font styles to use
Other font styles liked:
• brush lettering font in some parts

Requirements
Must have
• - Brush lettering font
• -Simple, a bit rustic design with some nice watercolor touch
• -Blogging Page
• -catchy yet fancy and elegant E-commerce page
Nice to have
• Well, I will let the designers use their skills and imaginations to the fullest.

```html
<!DOCTYPE html>
<html lang="en">
<head>
<meta charset="utf-8">
<title>Brewvine – Healthy With A Heart</title>
<link href="https://fonts.googleapis.com/css2?family=Montserrat:wght@400;500;600;700&family=Kaushan+Script&display=swap" rel="stylesheet">
<style>
:root{
  --parchment:#e6d6b4;
  --parchment-light:#efe4cc;
  --cream:#f4eee4;
  --bark:#4a2812;
  --bark-mid:#6a3a1c;
  --amber:#c8641c;
  --coral:#e86a4c;
  --chalk:#2f2f30;
  --ink:#2a2320;
  --white:#ffffff;
}
*{box-sizing:border-box;margin:0;padding:0}
html,body{width:1200px;height:2889px;overflow:hidden}
body{position:relative;font-family:"Montserrat",Arial,sans-serif;color:var(--ink);background:var(--parchment)}
.abs{position:absolute}
.script{font-family:"Kaushan Script",cursive;font-weight:400}

/* header */
.site-header{left:0;top:0;width:1200px;height:193px;background:linear-gradient(180deg,#eadbb9,#d9c49b)}
.top-links{right:150px;top:4px;display:flex;gap:28px;font-size:14px;color:var(--white);background:var(--bark);padding:4px 20px;border-radius:0 0 8px 8px;font-weight:500}
.top-links span{display:flex;align-items:center;gap:7px}
.logo{left:96px;top:28px}
.logo-name{font-size:44px;font-weight:700;color:var(--bark);display:flex;align-items:center;gap:10px}
.logo-name i{display:block;width:14px;height:14px;border-radius:50%;background:var(--amber)}
.logo-tag{font-size:14px;font-weight:600;color:var(--bark);letter-spacing:1px;margin-top:2px}
.search{left:862px;top:46px;width:240px;height:34px;background:var(--white);border-radius:18px;display:flex;align-items:center;justify-content:space-between;padding:0 16px;font-size:14px;color:#888}
.nav-bar{left:0;top:115px;width:1200px;height:47px;background:linear-gradient(180deg,var(--bark-mid),var(--bark))}
.nav{top:115px;height:47px;line-height:47px;font-size:17px;font-weight:600;color:var(--white);white-space:nowrap}
.teapot-deco{left:712px;top:66px;width:140px;height:96px;border-radius:48px 48px 20px 20px;background:radial-gradient(circle at 40% 55%,#8a4a22,#5f8a36 75%)}
.cart{left:866px;top:100px;width:244px;height:80px;background:linear-gradient(180deg,#e9dcc0,#cdb68b);border:3px solid var(--bark);display:flex;align-items:center;gap:14px;padding-left:28px}
.cart-title{font-size:15px;font-weight:700;color:var(--bark)}
.cart-sub{font-size:14px;font-weight:600;color:var(--bark)}

/* hero */
.hero{left:77px;top:200px;width:1050px;height:522px;background:linear-gradient(180deg,#5b3a1e,#8a6036 55%,#4a2c14);border-radius:6px}
.hero-title{left:77px;top:240px;width:1050px;text-align:center;font-size:58px;color:var(--white)}
.hero-photo{left:160px;top:330px;width:640px;height:340px;border-radius:12px;background:radial-gradient(ellipse at 50% 60%,#c99a5a,#9a6a34 55%,transparent 80%)}
.hero-copy{left:804px;top:356px;width:260px;color:var(--white)}
.hero-copy h2{font-size:24px;font-weight:600;margin-bottom:14px}
.hero-copy p{font-size:15px;line-height:1.5}
.btn-shop{display:inline-block;margin-top:22px;background:#c9a27a;color:var(--white);font-size:15px;font-weight:600;padding:7px 16px;border-radius:4px}
.hero-arrow{top:420px}

/* charity */
.charity{left:0;top:741px;width:1200px;height:222px;background:linear-gradient(180deg,#ecdcb0,#e2cf9e)}
.charity-line{left:0;top:808px;width:1200px;text-align:center;font-size:40px;color:var(--ink)}
.charity-line b{background:var(--coral);color:var(--white);font-weight:700;padding:0 8px}
.rule{top:832px;height:3px;width:140px;background:var(--ink);opacity:.7}
.charity-text{left:150px;top:860px;width:900px;text-align:center;font-size:20px;line-height:1.4}

/* featured */
.featured{left:0;top:963px;width:1200px;height:593px;background:repeating-linear-gradient(90deg,#7c4c28 0 120px,#6c4020 120px 122px,#85542e 122px 240px,#6c4020 240px 242px)}
.shelf{left:0;top:1490px;width:1200px;height:66px;background:linear-gradient(180deg,#8a5a30,#5a3418)}
.featured-title{left:0;top:1008px;width:1200px;text-align:center}
.featured-title span{display:inline-block;background:#1e1a18;color:var(--white);font-size:50px;padding:4px 40px;border-radius:30px}
.card{top:1111px;width:245px;height:386px;background:var(--white);box-shadow:0 4px 12px rgba(0,0,0,.4);text-align:center}
.card-photo{margin:36px auto 0;width:110px;height:170px;background:linear-gradient(180deg,#d9bd91,#b8955f);border-radius:4px}
.card-name{margin-top:42px;font-size:15px;font-weight:500}
.card-label{font-size:13px;color:#999;margin-top:6px}
.card-price{font-size:23px;font-weight:700;color:var(--amber);margin-top:2px}
.btn-cart{display:inline-block;margin-top:10px;background:linear-gradient(180deg,#7a4420,#4e2a12);color:var(--white);font-size:14px;padding:6px 22px;border-radius:16px}

/* welcome + blog */
.welcome{left:0;top:1556px;width:510px;height:524px;background:var(--chalk)}
.welcome-photo{left:0;top:1560px;width:170px;height:190px;background:radial-gradient(circle at 40% 40%,#3a5a2a,#1f2a1a 70%,transparent)}
.leaf-deco{left:420px;top:1512px;width:90px;height:90px;border-radius:50% 0;background:#4f8a2c}
.welcome-title{left:178px;top:1598px;color:var(--white);font-size:22px;font-weight:400}
.welcome-title span{font-size:36px}
.welcome-text{left:178px;top:1672px;width:300px;color:#e8e8e8;font-size:15px;line-height:1.6}
.blog{left:510px;top:1556px;width:690px;height:524px;background:var(--cream)}
.blog-head{left:542px;top:1584px;font-size:22px;font-weight:400}
.blog-head b{font-weight:700}
.post{left:548px;width:578px;height:160px}
.post-photo{width:212px;height:130px;border:5px solid var(--white);box-shadow:0 2px 6px rgba(0,0,0,.2)}
.post-date{left:232px;top:0;background:#ddd;font-size:12px;padding:2px 12px}
.post-title{left:232px;top:24px;width:340px;font-size:15px;font-weight:600;line-height:1.5}
.post-text{left:232px;top:76px;width:340px;font-size:13.5px;line-height:1.6;color:#333}
.post-text em{font-style:normal;color:var(--coral)}
.post-divider{left:548px;top:1812px;width:578px;height:1px;background:#d6cdbf}
.btn-blogs{left:543px;top:2004px;width:584px;height:34px;background:var(--coral);color:var(--white);font-size:15px;text-align:center;line-height:34px}

/* testimonials */
.testimonials{left:0;top:2080px;width:1200px;height:395px;background:#ebe7e2}
.testi-head{left:0;top:2128px;width:1200px;text-align:center;font-size:22px;font-weight:400}
.testi-head b{font-weight:700}
.quote{top:2185px;width:320px;text-align:center;font-size:14.5px;line-height:1.65;color:#444}
.quote-mark{font-size:48px;font-weight:700;color:#444;line-height:1;height:44px}
.quote-name{margin-top:14px;font-size:15px;font-weight:700;color:var(--ink)}

/* footer */
.footer{left:0;top:2475px;width:1200px;height:414px;background:linear-gradient(180deg,#a67c4a,#c79e68 20%)}
.footer-panel{left:70px;top:2504px;width:1057px;height:308px;background:var(--parchment-light)}
.col{top:2524px;font-size:14px;line-height:2.1}
.col h4{font-size:15px;font-weight:600;margin-bottom:4px;line-height:1.5}
.col p{color:#333}
.newsletter{left:645px;top:2504px;width:482px;height:308px;background:linear-gradient(180deg,#c9661c,#b2500f)}
.news-title{left:672px;top:2522px;color:var(--white);font-size:34px;line-height:1.15}
.news-text{left:672px;top:2620px;width:420px;color:var(--white);font-size:15px;line-height:1.5}
.email{left:676px;top:2690px;width:420px;height:42px;border-radius:21px;background:var(--white);font-size:14px;color:#666;padding-left:20px;line-height:42px}
.btn-signup{left:978px;top:2696px;width:112px;height:30px;border-radius:15px;background:var(--coral);color:var(--white);font-weight:700;font-size:15px;text-align:center;line-height:30px}
.touch{left:757px;top:2750px;display:flex;align-items:center;gap:10px;color:var(--white);font-size:15px;font-weight:500}
.touch i{display:block;width:32px;height:32px;border-radius:50%;border:2px solid var(--white)}
.cards{left:100px;top:2770px;display:flex;gap:4px}
.cards i{display:block;width:46px;height:28px;border-radius:3px}
.footer-teapot{left:362px;top:2770px;width:140px;height:84px;border-radius:42px 42px 18px 18px;background:radial-gradient(circle at 40% 55%,#8a4a22,#5f8a36 75%)}
.copyright{left:0;top:2862px;width:1200px;text-align:center;font-size:14px;color:var(--ink)}
</style>
</head>
<body>

<header class="abs site-header"></header>
<div class="abs top-links">
  <span><svg width="14" height="14" viewBox="0 0 14 14"><circle cx="7" cy="4" r="3" fill="#fff"/><path d="M1 14c0-4 3-6 6-6s6 2 6 6z" fill="#fff"/></svg>MY ACCOUNT</span>
  <span><svg width="12" height="14" viewBox="0 0 12 14"><rect x="1" y="6" width="10" height="8" fill="none" stroke="#fff" stroke-width="1.5"/><path d="M3 6V4a3 3 0 016 0v2" fill="none" stroke="#fff" stroke-width="1.5"/></svg>LOG IN</span>
</div>
<div class="abs logo">
  <div class="logo-name"><i></i>Brewvine</div>
  <div class="logo-tag">HEALTHY WITH A HEART</div>
</div>
<div class="abs search">Search
  <svg width="16" height="16" viewBox="0 0 16 16"><circle cx="6.5" cy="6.5" r="5" fill="none" stroke="#333" stroke-width="2"/><path d="M10.5 10.5L15 15" stroke="#333" stroke-width="2"/></svg>
</div>
<div class="abs nav-bar"></div>
<div class="abs teapot-deco" role="img" aria-label="Glass teapot and cup with green leaves"></div>
<nav>
  <span class="abs nav" style="left:100px">Home</span>
  <span class="abs nav" style="left:194px">About Us</span>
  <span class="abs nav" style="left:316px">Our Products</span>
  <span class="abs nav" style="left:472px">Blog</span>
  <span class="abs nav" style="left:555px">Contact Us</span>
</nav>
<div class="abs cart">
  <svg width="34" height="30" viewBox="0 0 34 30"><path d="M1 2h6l4 18h18l4-13H9" fill="none" stroke="#4a2812" stroke-width="2.5"/><circle cx="13" cy="26" r="2.5" fill="#4a2812"/><circle cx="27" cy="26" r="2.5" fill="#4a2812"/></svg>
  <div><div class="cart-title">MY CART</div><div class="cart-sub">0 item ($0.00)</div></div>
</div>

<section class="abs hero" role="img" aria-label="Rustic wooden backdrop with paper tea bags, a glass of amber tea, loose leaf tea and fresh tea leaves"></section>
<div class="abs hero-photo" role="img" aria-label="Paper tea bags beside a glass of tea and a bowl of loose leaf tea"></div>
<h1 class="abs hero-title script">Healthy With A Heart</h1>
<div class="abs hero-copy">
  <h2>Featured Teas</h2>
  <p>Lorem ipsum dolor sit amet, consectetur adipiscing elit</p>
  <span class="btn-shop">Shop Now</span>
</div>
<svg class="abs hero-arrow" style="left:88px" width="50" height="44" viewBox="0 0 50 44"><path d="M40 8C22 6 12 14 10 24M10 24l-6-8M10 24l9-5" fill="none" stroke="#fff" stroke-width="3"/></svg>
<svg class="abs hero-arrow" style="left:1062px" width="50" height="44" viewBox="0 0 50 44"><path d="M10 8c18-2 28 6 30 16M40 24l6-8M40 24l-9-5" fill="none" stroke="#fff" stroke-width="3"/></svg>

<section class="abs charity"></section>
<div class="abs rule" style="left:95px"></div>
<div class="abs rule" style="left:965px"></div>
<div class="abs charity-line"><b>EVERY 20%</b> from the total amount</div>
<p class="abs charity-text">of the customer's purchase from our website always goes back to their communities to help build better sanitation, education or whatever they need.</p>

<section class="abs featured"></section>
<div class="abs shelf"></div>
<h2 class="abs featured-title"><span class="script">Featured Products</span></h2>
<div class="abs card" style="left:73px"><div class="card-photo" role="img" aria-label="Kraft paper tea pouch with window"></div><div class="card-name">Product Name</div><div class="card-label">Price</div><div class="card-price">$25.99</div><span class="btn-cart">Add to Cart</span></div>
<div class="abs card" style="left:343px"><div class="card-photo" role="img" aria-label="Kraft paper tea pouch with window"></div><div class="card-name">Product Name</div><div class="card-label">Price</div><div class="card-price">$25.99</div><span class="btn-cart">Add to Cart</span></div>
<div class="abs card" style="left:612px"><div class="card-photo" role="img" aria-label="Kraft paper tea pouch with window"></div><div class="card-name">Product Name</div><div class="card-label">Price</div><div class="card-price">$25.99</div><span class="btn-cart">Add to Cart</span></div>
<div class="abs card" style="left:882px"><div class="card-photo" role="img" aria-label="Kraft paper tea pouch with window"></div><div class="card-name">Product Name</div><div class="card-label">Price</div><div class="card-price">$25.99</div><span class="btn-cart">Add to Cart</span></div>

<section class="abs welcome"></section>
<div class="abs welcome-photo" role="img" aria-label="Cast iron teapot, cups and green leaves on a mat"></div>
<h2 class="abs welcome-title">Welcome to <span class="script">Brewvine</span></h2>
<div class="abs welcome-text">
  <p>Lorem ipsum dolor sit amet, consectetur adipiscing elit, sed do eiusmod tempor incididunt ut labore et dolore magna aliqua. Ut enim ad minim veniam, quis nostrud exercitation ullamco laboris nisi ut aliquip ex ea commodo consequat. Duis aute irure dolor in reprehenderit in voluptate velit esse cillum dolore eu fugiat nulla pariatur. Excepteur sint occaecat cupidatat non proident, sunt in culpa qui officia deserunt mollit anim id est laborum.</p>
  <p style="margin-top:18px">Duis aute irure dolor in reprehenderit in voluptate velit esse cillum dolore eu fugiat nulla pariatur.</p>
</div>
<section class="abs blog"></section>
<div class="abs leaf-deco" role="img" aria-label="Green tea leaf"></div>
<h2 class="abs blog-head">Latest <b>Blog</b></h2>
<article class="abs post" style="top:1655px">
  <div class="post-photo" style="background:linear-gradient(180deg,#8aa048,#4f6a22)" role="img" aria-label="Cups of green tea on a bamboo mat"></div>
  <span class="abs post-date">18 Mar, 2017</span>
  <div class="abs post-title">Lorem ipsum dolor sit amet, consectetur adipiscing elit,</div>
  <div class="abs post-text">sed do eiusmod tempor incididunt ut labore et dolore magna aliqua. Ut enim ad minim veniam, quis nostrud exercitation. <em>Read more</em></div>
</article>
<div class="abs post-divider"></div>
<article class="abs post" style="top:1835px">
  <div class="post-photo" style="background:linear-gradient(180deg,#c88a2a,#6a4a1a)" role="img" aria-label="Glass teapot of green tea in warm light"></div>
  <span class="abs post-date">18 Mar, 2017</span>
  <div class="abs post-title">Lorem ipsum dolor sit amet, consectetur adipiscing elit,</div>
  <div class="abs post-text">sed do eiusmod tempor incididunt ut labore et dolore magna aliqua. Ut enim ad minim veniam, quis nostrud exercitation. <em>Read more</em></div>
</article>
<div class="abs btn-blogs">View More Blogs</div>

<section class="abs testimonials"></section>
<div class="abs rule" style="left:70px;top:2140px;width:365px;height:2px"></div>
<div class="abs rule" style="left:765px;top:2140px;width:365px;height:2px"></div>
<h2 class="abs testi-head">What Others Are <b>Saying</b></h2>
<blockquote class="abs quote" style="left:78px"><div class="quote-mark">&ldquo;</div>Lorem ipsum dolor sit amet, consectetur adipiscing elit, sed do eiusmod tempor incididunt ut labore et dolore magna aliqua. Ut enim ad minim veniam.<div class="quote-name">- Marcus Hale</div></blockquote>
<blockquote class="abs quote" style="left:440px"><div class="quote-mark">&ldquo;</div>Lorem ipsum dolor sit amet, consectetur adipiscing elit, sed do eiusmod tempor incididunt ut labore et dolore magna aliqua. Ut enim ad minim veniam, quis nostrud exercitation ullamco laboris nisi ut aliquip ex ea commodo consequat.<div class="quote-name" style="margin-top:26px">- Tobias Reed</div></blockquote>
<blockquote class="abs quote" style="left:800px"><div class="quote-mark">&ldquo;</div>Lorem ipsum dolor sit amet, consectetur adipiscing elit, sed do eiusmod tempor incididunt ut labore et dolore magna aliqua. Ut enim ad minim veniam, quis nostrud exercitation ullamco laboris nisi<div class="quote-name">- Daniel Pryce</div></blockquote>

<footer class="abs footer"></footer>
<div class="abs footer-panel"></div>
<div class="abs col" style="left:100px"><h4>Information</h4><p>Home<br>About Us<br>Our Products<br>Blog<br>Contact Us</p></div>
<div class="abs col" style="left:243px;line-height:1.55"><h4 style="line-height:2.1">Contact Us</h4><p>Brewvine<br>Street Name, 000000<br>City Name</p><p style="margin-top:10px">info@brewvine.com</p><p style="margin-top:10px">555-014-2270</p><p style="margin-top:24px">View Map</p></div>
<div class="abs col" style="left:443px"><h4>Customer Service</h4><p>My Account<br>Referral Program<br>General Policies<br>Legal<br>Privacy Policy<br>FAQ</p></div>
<div class="abs cards"><i style="background:#1a3a8a"></i><i style="background:#2a5aa8"></i><i style="background:#d8d8d8"></i><i style="background:#3a7ac8"></i><i style="background:#e6e6e6"></i></div>
<div class="abs footer-teapot" role="img" aria-label="Glass teapot and cup with green leaves"></div>
<section class="abs newsletter"></section>
<h2 class="abs news-title script">Join Our Community!<br>Sign Up for Our Newsletter.</h2>
<p class="abs news-text">Lorem ipsum dolor sit amet, consectetur adipiscing elit, sed do eiusmod tempor magna aliqua.</p>
<div class="abs email">Enter your email address</div>
<div class="abs btn-signup">SIGN UP</div>
<div class="abs touch">Get In Touch <i></i><i></i><i></i></div>
<p class="abs copyright">© 2017 Brewvine. All Rights Reserved</p>

</body>
</html>
```